Northwind Crown Hair Supply needs a packaging design

We need a packaging design for a new hair extension company based in Edmonton, Alberta called Velvet Strands. Our packaging should communicate high quality, luxurious hair that will never tangle or dry out. The product will be marketed to salon professionals as well as clients. There must be an opening to see the hair from the outside.

Our advertising campaign is going to be based on boho chic; Dorian Keswick/ Open Meadow/Tumbling Echo.

Target Market(s)

Women and beauty industry professionals. High end market.

Industry/Entity Type

Advertising

Requirements
Must have
• "Highest quality 100% Remi hair!" should be written on the front of the package. In addition, we would like to add text to the back or inside of the packaging as follows:
• Hair Collection and Color Processing:
• Only the highest quality hair is selected which ensures high moisture and nutrient content
• The hair is directly cut from the donor which ensures that the hair cuticle remains intact and always tangle-free
• No chemicals are used in dyeing the hair
• The hair will never fade due to the mild and healthy herbal extract used in the dyeing process which gently penetrates to the inner core of the hair
• Care Instructions:
• Velvet Strands provides only the highest in quality Remi hair that demands very little care to maintain it’s luxurious feel.
• Use a proper extension bristle brush
• Wash the hair with a sulfate-free shampoo and follow with a moisturizing conditioner that is formulated for hair extensions
• Do not apply any type of chemicals to the hair
• We proudly show our immense passion for delivering superior quality in our full product line.
• We insist that it is important for you to know and understand what you are purchasing in your hair extensions. We guarantee the highest quality of our products.
• Velvet Strands is strongly committed to serving their clients with utmost integrity, believing in a foundation of personal and professional ethics and our 20 years service in the beauty industry.

```html
<!DOCTYPE html>
<html lang="en">
<head>
<meta charset="utf-8">
<title>Velvet Strands – Tube Packaging Concepts</title>
<link rel="stylesheet" href="https://fonts.googleapis.com/css2?family=Roboto:wght@400;700&display=swap">
<style>
  :root {
    --paper: #ffffff;
    --ink: #222222;
    --wine-edge: #3a0e24;
    --wine-mid: #6e2148;
    --wine-glow: #8a3660;
    --wine-deep: #4a1430;
    --wine-rim: #5e1b3d;
    --band: #121212;
    --gold: #f0d400;
    --label-text: #f4f4f4;
    --stitch: #8a8a8a;
    --window: #ffffff;
  }
  * { margin: 0; padding: 0; box-sizing: border-box; }
  html, body { width: 1200px; height: 877px; overflow: hidden; background: var(--paper); }
  body { font-family: "Roboto", Arial, sans-serif; color: var(--ink); }

  .canvas { position: relative; width: 1200px; height: 877px; overflow: hidden; }
  .stage { position: absolute; top: 0; left: 0; width: 1157px; height: 846px; transform: scale(1.0372); transform-origin: 0 0; }
  .artwork { position: absolute; inset: 0; }

  .design-title { position: absolute; font-size: 10px; letter-spacing: 0.5px; color: var(--ink); }
  .design-title--one { left: 110px; top: 19px; }
  .design-title--two { left: 905px; top: 14px; }

  .window-note { position: absolute; left: 470px; top: 486px; width: 218px; text-align: right; font-size: 10px; line-height: 12px; color: var(--ink); }

  .stop-edge { stop-color: var(--wine-edge); }
  .stop-mid { stop-color: var(--wine-mid); }
  .stop-glow { stop-color: var(--wine-glow); }

  .tube-body { fill: url(#wineShade); }
  .tube-lid { fill: var(--wine-deep); }
  .tube-lid-inner { fill: var(--wine-rim); }
  .tube-band { fill: var(--band); }
  .pull-tab { fill: var(--band); }
  .pull-tab-hole { fill: var(--wine-deep); }
  .band-text { fill: var(--gold); font-size: 11.5px; font-family: "Roboto", Arial, sans-serif; }

  .brand-plate { fill: var(--band); }
  .brand-stitch { fill: none; stroke: var(--stitch); stroke-width: 0.8; stroke-dasharray: 2 2; }
  .brand-dot { fill: var(--label-text); }
  .brand-name { fill: var(--label-text); font-size: 16px; font-family: "Roboto", Arial, sans-serif; }
  .brand-tagline { fill: var(--label-text); font-size: 10.5px; font-family: "Roboto", Arial, sans-serif; }

  .view-window { fill: var(--window); stroke: var(--band); stroke-width: 6; }

  .info-panel { position: absolute; background: var(--band); color: var(--label-text); padding: 6px 8px; font-size: 5px; line-height: 6.1px; text-align: center; overflow: hidden; }
  .info-panel::after { content: ""; position: absolute; inset: 3px; border: 0.7px dashed var(--stitch); pointer-events: none; }
  .info-panel h3 { font-size: 6.2px; font-weight: 700; margin: 4px 0 5px; }
  .info-panel p { margin-bottom: 3.5px; }

  .info-panel--collection-a { left: 283px; top: 304px; width: 172px; height: 106px; }
  .info-panel--care-a { left: 283px; top: 414px; width: 172px; height: 194px; }
  .info-panel--collection-b { left: 930px; top: 294px; width: 170px; height: 106px; }
  .info-panel--care-b { left: 930px; top: 404px; width: 170px; height: 196px; }
</style>
</head>
<body>
<div class="canvas">
  <div class="stage">
    <svg class="artwork" width="1157" height="846" viewBox="0 0 1157 846" xmlns="http://www.w3.org/2000/svg">
      <defs>
        <linearGradient id="wineShade" x1="0" y1="0" x2="1" y2="0">
          <stop offset="0" class="stop-edge"/>
          <stop offset="0.3" class="stop-mid"/>
          <stop offset="0.5" class="stop-glow"/>
          <stop offset="0.72" class="stop-mid"/>
          <stop offset="1" class="stop-edge"/>
        </linearGradient>
        <path id="arcTop1" d="M6,226 A91.5,16 0 0 0 177,226"/>
        <path id="arcTop3" d="M6,232 A91.5,16 0 0 0 177,232"/>
        <path id="arcBottom" d="M6,740 A91.5,16 0 0 0 177,740"/>
      </defs>

      <!-- Design 1, front -->
      <g class="tube tube--front" transform="translate(45,0)">
        <path class="pull-tab" d="M86,146 C78,110 100,72 114,58 C122,72 114,118 103,146 Z"/>
        <path class="pull-tab-hole" d="M95,116 C95,98 104,82 111,72 C113,86 109,102 100,120 Z"/>
        <path class="tube-body" role="img" aria-label="Wine damask pattern wrapping the tube" d="M0,143 L0,760 A91.5,16 0 0 0 183,760 L183,143 Z"/>
        <ellipse class="tube-lid" cx="91.5" cy="143" rx="91.5" ry="16"/>
        <ellipse class="tube-lid-inner" cx="91.5" cy="144" rx="82" ry="12"/>
        <path class="tube-band" d="M0,200 A91.5,16 0 0 0 183,200 L183,240 A91.5,16 0 0 1 0,240 Z"/>
        <text class="band-text"><textPath href="#arcTop1" startOffset="50%" text-anchor="middle">Highest quality 100% Remi hair</textPath></text>
        <path class="tube-band" d="M0,705 A91.5,16 0 0 0 183,705 L183,760 A91.5,16 0 0 1 0,760 Z"/>
        <text class="band-text"><textPath href="#arcBottom" startOffset="50%" text-anchor="middle">High quality, Luxurious, No Tangles</textPath></text>
        <g class="brand-label">
          <rect class="brand-plate" x="20" y="318" width="142" height="84" rx="12"/>
          <rect class="brand-stitch" x="25" y="323" width="132" height="74" rx="9"/>
          <circle class="brand-dot" cx="91.5" cy="338" r="5"/>
          <text class="brand-name" x="91.5" y="364" text-anchor="middle">Velvet Strands</text>
          <text class="brand-tagline" x="91.5" y="384" text-anchor="middle">Premium Hair Extension</text>
        </g>
      </g>

      <!-- Design 1, back -->
      <g class="tube tube--back" transform="translate(275,0)">
        <path class="pull-tab" d="M90,146 C82,110 106,74 122,60 C128,74 118,118 106,146 Z"/>
        <path class="pull-tab-hole" d="M99,116 C100,98 110,84 118,74 C119,88 113,104 104,120 Z"/>
        <path class="tube-body" role="img" aria-label="Wine damask pattern wrapping the tube" d="M0,143 L0,760 A91.5,16 0 0 0 183,760 L183,143 Z"/>
        <ellipse class="tube-lid" cx="91.5" cy="143" rx="91.5" ry="16"/>
        <ellipse class="tube-lid-inner" cx="91.5" cy="144" rx="82" ry="12"/>
        <path class="tube-band" d="M0,172 A91.5,16 0 0 0 183,172 L183,214 A91.5,16 0 0 1 0,214 Z"/>
        <path class="tube-band" d="M0,705 A91.5,16 0 0 0 183,705 L183,760 A91.5,16 0 0 1 0,760 Z"/>
      </g>

      <!-- Design 2, front -->
      <g class="tube tube--window" transform="translate(690,0)">
        <path class="pull-tab" d="M88,146 C80,112 100,78 112,66 C120,80 112,120 103,146 Z"/>
        <path class="pull-tab-hole" d="M96,118 C96,102 104,88 110,80 C112,92 108,106 100,122 Z"/>
        <path class="tube-body" role="img" aria-label="Wine damask pattern wrapping the tube" d="M0,143 L0,760 A91.5,16 0 0 0 183,760 L183,143 Z"/>
        <ellipse class="tube-lid" cx="91.5" cy="143" rx="91.5" ry="16"/>
        <ellipse class="tube-lid-inner" cx="91.5" cy="144" rx="82" ry="12"/>
        <path class="tube-band" d="M0,205 A91.5,16 0 0 0 183,205 L183,246 A91.5,16 0 0 1 0,246 Z"/>
        <text class="band-text"><textPath href="#arcTop3" startOffset="50%" text-anchor="middle">Highest quality 100% Remi hair</textPath></text>
        <path class="tube-band" d="M0,705 A91.5,16 0 0 0 183,705 L183,760 A91.5,16 0 0 1 0,760 Z"/>
        <text class="band-text"><textPath href="#arcBottom" startOffset="50%" text-anchor="middle">High quality, Luxurious, No Tangles</textPath></text>
        <g class="brand-label">
          <rect class="brand-plate" x="20" y="320" width="142" height="82" rx="12"/>
          <rect class="brand-stitch" x="25" y="325" width="132" height="72" rx="9"/>
          <circle class="brand-dot" cx="91.5" cy="339" r="5"/>
          <text class="brand-name" x="91.5" y="365" text-anchor="middle">Velvet Strands</text>
          <text class="brand-tagline" x="91.5" y="385" text-anchor="middle">Premium Hair Extension</text>
        </g>
        <rect class="view-window" x="18" y="420" width="147" height="252" rx="16"/>
      </g>

      <!-- Design 2, back -->
      <g class="tube tube--back" transform="translate(920,0)">
        <path class="pull-tab" d="M90,146 C82,112 104,78 120,64 C126,78 116,120 105,146 Z"/>
        <path class="pull-tab-hole" d="M98,118 C99,100 108,86 116,78 C117,92 112,106 103,122 Z"/>
        <path class="tube-body" role="img" aria-label="Wine damask pattern wrapping the tube" d="M0,143 L0,760 A91.5,16 0 0 0 183,760 L183,143 Z"/>
        <ellipse class="tube-lid" cx="91.5" cy="143" rx="91.5" ry="16"/>
        <ellipse class="tube-lid-inner" cx="91.5" cy="144" rx="82" ry="12"/>
        <path class="tube-band" d="M0,178 A91.5,16 0 0 0 183,178 L183,218 A91.5,16 0 0 1 0,218 Z"/>
        <path class="tube-band" d="M0,705 A91.5,16 0 0 0 183,705 L183,760 A91.5,16 0 0 1 0,760 Z"/>
      </g>
    </svg>

    <div class="design-title design-title--one">DESIGN 1</div>
    <div class="design-title design-title--two">DESIGN 2</div>

    <p class="window-note">This white area will be<br>transparent&nbsp; from frontside<br>Hair Extension should be visible here</p>

    <section class="info-panel info-panel--collection-a">
      <h3>Hair Collection and Color Processing:</h3>
      <p>Only the highest quality hair is selected<br>Which ensures high moisture and nutrient content</p>
      <p>The hair is directly cut from the donor which ensures that the hair cuticle remains intact and always tangle-free</p>
      <p>No chemicals are used in dyeing the hair</p>
      <p>The hair will never fade due to the mild and healthy herbal extract used in the dyeing process which gently penetrates to the innercore of the hair</p>
    </section>
    <section class="info-panel info-panel--care-a">
      <h3>Care Instructions:</h3>
      <p>Velvet Strands provides only the highest in quality Remi hair that demands very little care to maintain it's luxurious feel.</p>
      <p>Use a proper extension bristle brush</p>
      <p>Wash the hair with a sulfate-free shampoo and follow a moisturizing conditioner that is formulated for hair extensions</p>
      <p>Do not apply any type of chemicals to the hair</p>
      <p>We proudly show our immense PASSION for delivering superior quality in our full product line.</p>
      <p>We insist that it is important for you to know and understand what you are purchasing in Your hair extensions.</p>
      <p>We guarantee the highest quality of our products. Velvet Strands is strongly committed to serving their</p>
      <p>clients with utmost integrity, believing in a foundation of personal and professional ethics and our 20 years service in the beauty industry</p>
    </section>

    <section class="info-panel info-panel--collection-b">
      <h3>Hair Collection and Color Processing:</h3>
      <p>Only the highest quality hair is selected<br>Which ensures high moisture and nutrient content</p>
      <p>The hair is directly cut from the donor which ensures that the hair cuticle remains intact and always tangle-free</p>
      <p>No chemicals are used in dyeing the hair</p>
      <p>The hair will never fade due to the mild and healthy herbal extract used in the dyeing process which gently penetrates to the innercore of the hair</p>
    </section>
    <section class="info-panel info-panel--care-b">
      <h3>Care Instructions:</h3>
      <p>Velvet Strands provides only the highest in quality Remi hair that demands very little care to maintain it's luxurious feel.</p>
      <p>Use a proper extension bristle brush</p>
      <p>Wash the hair with a sulfate-free shampoo and follow a moisturizing conditioner that is formulated for hair extensions</p>
      <p>Do not apply any type of chemicals to the hair</p>
      <p>We proudly show our immense PASSION for delivering superior quality in our full product line.</p>
      <p>We insist that it is important for you to know and understand what you are purchasing in Your hair extensions.</p>
      <p>We guarantee the highest quality of our products. Velvet Strands is strongly committed to serving their</p>
      <p>clients with utmost integrity, believing in a foundation of personal and professional ethics and our 20 years service in the beauty industry</p>
    </section>
  </div>
</div>
</body>
</html>
```